Poster for a contemporary concert and Tango-Milonga

We are a German-based ensemble specialising in contemporary classical music, and are currently seeking an artist to design a poster promoting our forthcoming crossover concert mixing contemporary art music with tango. Although much of our work concentrates on traditional concert formats, with an ensemble on stage in front of a seated audience, we also frequently perform in more relaxed or alternative environments. This concert will be amongst our more extravagant presentations, aiming at a broad, popular audience. The evening will begin with performances of experimental concert works. Its centrepiece will be a screening of the Vardoni/Kess tour de force "Le Renard Opaque", complemented by a vigorous and edgy performance of a work composed especially for our ensemble by the prominent composer Tomas Bervago. The concert performance is dominated by art music drawing on tango and popular dance styles, with the formal concert atmosphere transitioning over the course of the evening into a milonga dance extravaganza, the entire audience being free to participate in dancing to our own live musical accompaniment of tango Argentino, interspersed with offerings from a local DJ.
The conceptual link between the concert and the milonga is the film "Le Renard Opaque", one of the greatest and most influential films of the "roaring 20s", which premièred to an experimental mixture of the gravitas of German Romantic music and the vigour of Argentine tango.

We are looking for a poster that gives prominence both to the experimental, avant garde nature of our concert performance and to the popular tango element, while tying in with the themes and aesthetic of the film "Le Renard Opaque". The challenge to you as designers lies in combining these three elements. One suggestion would be to use the aesthetics of the film (black & white, surrealistic), combined with a striking tango motif. Of course, any and all suggestions are welcome – whatever excites your flair and creativity, and we are more than happy to provide any further details should you so require.

The film is available for viewing on youtube, while our logo is attached to this call for proposals. Feel free to visit our website at www.ensemblevitrona.de.
Updates

Hello all, We're very impressed with the designs so far. Two aspects are very important that wouldn't have been clear from the original brief, and if it isn't too much to ask. Firstly, we need the words "Konzert", "El Zorro Opaco" (or "Le Renard Opaque") and "Tango" to be clearly visible at first glance. Secondly, as purveyors of contemporary music, we tend to prefer sans serif or at least fairly stark fonts over florid ones. Thankyou very much for your excellent work so far.

Target Market(s)

adults based in Dresden/Germany either interested in classical concerts or dance events

Industry/Entity Type

Call

Colors

Designer to choose colors to be used in the design.

Requirements
Must have
• The following must be clearly visible on the poster:
- date: "21. Mai 2015", "21.05.2015" or "Do., 21. Mai"
- time: "19:30 Uhr"
- additional info: "Tangokurs für Anfänger 18 Uhr"
- place: "Lichthalle Dresden" or "Lichthalle"
- music: "El Zorro Opaco" or "Ensemble El Zorro Opaco"
- the logos of our sponsors: "mtrw", "Forum Dresden" and "Tonbogen Dresden"

```html
<!DOCTYPE html>
<html lang="de">
<head>
<meta charset="utf-8">
<title>Ensemble El Zorro Opaco – Tango</title>
<link rel="stylesheet" href="https://fonts.googleapis.com/css2?family=Oswald:wght@400;500&family=Yellowtail&family=Roboto:wght@300;400&display=swap">
<style>
  :root {
    --page: #dcdbd8;
    --ink-black: #0b0b0b;
    --ink-dark: #2a2a2a;
    --photo-mid: #4a4a4a;
    --photo-light: #8a8a8a;
    --paper: #ffffff;
    --title-face: #f4f4f4;
    --title-depth: #6d6d6d;
    --title-deep: #3a3a3a;
    --footer-text: #333333;
    --footer-muted: #8c8c8c;
  }
  * { margin: 0; padding: 0; box-sizing: border-box; }
  html, body {
    width: 1200px;
    height: 1148px;
    overflow: hidden;
    background: var(--page);
  }
  .poster {
    position: absolute;
    left: 205px;
    top: 32px;
    width: 790px;
    height: 1084px;
    background: var(--ink-black);
    overflow: hidden;
  }
  .poster__photo {
    position: absolute;
    inset: 0;
    background:
      radial-gradient(ellipse 38% 30% at 62% 45%, var(--photo-light) 0%, rgba(90,90,90,0.5) 45%, rgba(0,0,0,0) 100%),
      radial-gradient(ellipse 60% 55% at 55% 55%, var(--photo-mid) 0%, var(--ink-dark) 55%, var(--ink-black) 100%);
  }
  .title {
    position: absolute;
    left: 30px;
    top: 110px;
    width: 720px;
    font-family: "Yellowtail", cursive;
    font-weight: 400;
    color: var(--title-face);
    transform: rotate(-4deg);
    transform-origin: left top;
    text-shadow:
      1px 1px 0 var(--title-depth),
      2px 2px 0 var(--title-depth),
      3px 3px 0 var(--title-depth),
      4px 4px 0 var(--title-depth),
      5px 5px 0 var(--title-deep),
      6px 6px 0 var(--title-deep),
      8px 10px 10px rgba(0,0,0,0.8);
  }
  .title__ensemble {
    display: block;
    font-size: 60px;
    line-height: 1;
  }
  .title__name {
    display: block;
    margin-left: 45px;
    margin-top: -2px;
    font-size: 84px;
    line-height: 1;
    white-space: nowrap;
  }
  .details {
    position: absolute;
    left: 66px;
    top: 672px;
    font-family: "Oswald", sans-serif;
    color: var(--paper);
    text-transform: uppercase;
  }
  .details__kicker {
    font-size: 25px;
    line-height: 1.1;
    font-weight: 500;
  }
  .details__headline {
    font-size: 60px;
    line-height: 1.05;
    font-weight: 500;
    margin-bottom: 6px;
  }
  .details__line {
    font-size: 24px;
    line-height: 1.45;
    font-weight: 400;
  }
  .sponsors {
    position: absolute;
    left: 34px;
    top: 960px;
    width: 620px;
    height: 90px;
    background: var(--paper);
    display: flex;
    align-items: center;
    justify-content: space-between;
    padding: 0 30px;
    font-family: "Roboto", sans-serif;
    color: var(--footer-text);
  }
  .sponsor {
    display: flex;
    align-items: center;
    gap: 8px;
  }
  .sponsor__mark {
    width: 22px;
    height: 22px;
    border: 2px solid var(--footer-text);
  }
  .sponsor__mark--filled {
    width: 16px;
    height: 30px;
    border: none;
    background: var(--footer-text);
  }
  .sponsor__name {
    font-size: 15px;
    font-weight: 400;
  }
  .sponsor__funding {
    text-align: right;
    line-height: 1.15;
  }
  .sponsor__funding-note {
    display: block;
    font-size: 13px;
    font-weight: 300;
    color: var(--footer-muted);
  }
  .sponsor__funding-name {
    display: block;
    font-size: 15px;
    font-weight: 400;
  }
</style>
</head>
<body>
  <main class="poster">
    <div class="poster__photo" role="img" aria-label="Black and white photograph of a tango couple dancing in close embrace under falling rain"></div>

    <h1 class="title">
      <span class="title__ensemble">Ensemble</span>
      <span class="title__name">El Zorro Opaco</span>
    </h1>

    <section class="details">
      <p class="details__kicker">Contemporary</p>
      <p class="details__kicker">Art Music with</p>
      <p class="details__headline">Tango</p>
      <p class="details__line">21. Mai 2015</p>
      <p class="details__line">19:30 Uhr</p>
      <p class="details__line">Tangokurs für Anfänger 18 Uhr</p>
      <p class="details__line">Lichthalle Dresden</p>
    </section>

    <footer class="sponsors">
      <div class="sponsor">
        <span class="sponsor__mark"></span>
        <span class="sponsor__name">mtrw</span>
      </div>
      <div class="sponsor">
        <span class="sponsor__funding">
          <span class="sponsor__funding-note">gefördert durch das</span>
          <span class="sponsor__funding-name">Forum Dresden</span>
        </span>
        <span class="sponsor__mark sponsor__mark--filled"></span>
      </div>
      <div class="sponsor">
        <span class="sponsor__mark"></span>
        <span class="sponsor__name">Tonbogen Dresden</span>
      </div>
    </footer>
  </main>
</body>
</html>
```